Renny Osbert Personalised Health, Performance and Longevity Exec Coach

Business Card for www.rennyosbert.example site. It is a trust site and I use it for 1:1 relatable connections. It is the one I use for building intimate 1:1 trust building and Exec Coaching Services and programs for high wealth individuals and corporates. I also have a commercial programmatic site of my personal health products and services and programs for main stream one to many. www.halfwaypioneer.example that can also provoke thought for the www.rennyosbert.example business card. (mind you will get a separate business card for that site, but want to provide context). It has a logo which you may want to draw from in designing the rennyosbert business card which is personal and is about building my brand. There is also a rennyosbert personal Chirply page and rennyosbert business Chirply page. I am a Certified Talent Compass 3.1 Coach with Verrow and you can get a corporate brief of me on there to give you more context https://www.verrowtalenthub.example/coach/en-us/directory?search=renny

Target Market(s)

Being a Personalised Health Coach I am focused on Health>Performance>Longevity>Wellbeing. Target market is Executives /High Wealth individuals/Corporates. I am most relatable to the IT industry as I was ion it building partnerships for IT companies for 28+ years.

Industry/Entity Type

Health And Wellness

Contact Information for Business Card

Name: Renny Osbert
email: renny@rennyosbert.example
Phone: Australia +61 491352864 Singapore +65 83426109

Font styles to use
Sans Serif
Other font styles liked:
• Arial and Calibra could work?

Colors

Designer to choose colors to be used in the design.

Requirements
Must have
• It must be a no BS design that is intimate. In keeping with the rennyosbert.example website I'm guessing grey scale. It may be printed on plastic as well for durability and a point of difference. It must have people feeling trust and feeling safe to be 1:1 personal. It's about helping people move from stuck to sustainable change. Moving them to a healthier state, increasing performance if and where they want, longevity and well being.
Nice to have
• On the back you can place a logo that is in line with what I have as a colourful mandala at www.halfwaypioneer.example. It will be on the landing page and top left of each page in that site. A greyscale simpler version to create linkage to my philosophy. Also you could have the continuum of Personalised Health > > Performance > Longevity > Wellbeing as well or instead of in your designs some how infographcially represented if not using the existing logo at Halfwaypioneer.example
Should not have
• Clutter is a no no. Keep it clean, easy to read, no BS feel. Must be authentic and warm yet smart.

```html
<!DOCTYPE html>
<html lang="en">
<head>
<meta charset="utf-8">
<title>Renny Osbert – Business Card</title>
<link href="https://fonts.googleapis.com/css2?family=Roboto:wght@400;500&family=Montserrat:wght@500&display=swap" rel="stylesheet">
<style>
  :root {
    --backdrop: #3b3b3b;
    --card-dark: #121212;
    --card-light: #f7f7f5;
    --ink-light: #f2f2f2;
    --ink-dark: #161616;
    --mark-light: #d9d9d9;
    --mark-mid: #8a8a8a;
  }
  * { margin: 0; padding: 0; box-sizing: border-box; }
  html, body {
    width: 799px; height: 1200px; overflow: hidden;
    background: var(--backdrop);
    font-family: "Roboto", Arial, sans-serif;
  }
  .card {
    position: absolute;
    left: 120px;
    width: 560px; height: 320px;
    box-shadow: 0 6px 18px rgba(0,0,0,.45);
  }
  .card--front { top: 140px; background: var(--card-dark); color: var(--ink-light); }
  .card--back { top: 740px; background: var(--card-light); color: var(--ink-dark); }

  .brand-mark {
    position: absolute;
    left: 50%; top: 30px;
    transform: translateX(-50%);
    display: flex; flex-direction: column; align-items: center; gap: 10px;
  }
  .brand-mark__disc {
    width: 130px; height: 130px; border-radius: 50%;
    background: radial-gradient(circle, var(--mark-light) 0%, var(--mark-mid) 70%, #4a4a4a 100%);
  }
  .brand-mark__name {
    font-size: 13px; font-weight: 400; color: var(--ink-light); letter-spacing: .5px;
  }
  .focus {
    position: absolute; left: 58px; top: 222px;
    font-size: 15px; line-height: 24px; font-weight: 400;
  }

  .holder-name {
    position: absolute; right: 58px; top: 64px;
    font-family: "Montserrat", Arial, sans-serif;
    font-weight: 500; font-size: 26px; letter-spacing: 1.5px;
    text-transform: uppercase;
  }
  .contact-list {
    position: absolute; left: 44px; bottom: 44px;
    list-style: none; font-size: 14px; line-height: 19px;
  }
  .contact-list li { display: flex; align-items: center; gap: 12px; }
  .contact-list svg { width: 12px; height: 12px; flex: none; }
</style>
</head>
<body>

<section class="card card--front">
  <div class="brand-mark" role="img" aria-label="Halfwaypioneer philosophy mark in greyscale">
    <div class="brand-mark__disc"></div>
    <span class="brand-mark__name">Halfwaypioneer</span>
  </div>
  <p class="focus">
    Being a Personalised Health Coach I am focused on<br>
    Health&nbsp; | &nbsp;Performance&nbsp; | &nbsp;Longevity&nbsp; | &nbsp;Wellbeing
  </p>
</section>

<section class="card card--back">
  <h1 class="holder-name">Renny Osbert</h1>
  <ul class="contact-list">
    <li>
      <svg viewBox="0 0 12 12" aria-hidden="true"><circle cx="6" cy="6" r="5.3" fill="none" stroke="currentColor" stroke-width="1.2"/><path d="M4 3.2l1 .1.5 1.3-.7.6c.3.7.8 1.2 1.5 1.5l.6-.7 1.3.5.1 1c-2.6.3-4.6-1.7-4.3-4.3z" fill="currentColor"/></svg>
      <span>+61 491352864 (Australia)</span>
    </li>
    <li>
      <svg viewBox="0 0 12 12" aria-hidden="true"><circle cx="6" cy="6" r="5.3" fill="none" stroke="currentColor" stroke-width="1.2"/><path d="M4 3.2l1 .1.5 1.3-.7.6c.3.7.8 1.2 1.5 1.5l.6-.7 1.3.5.1 1c-2.6.3-4.6-1.7-4.3-4.3z" fill="currentColor"/></svg>
      <span>+65 83426109 (Singapore)</span>
    </li>
    <li>
      <svg viewBox="0 0 12 12" aria-hidden="true"><rect x="0.8" y="2.3" width="10.4" height="7.4" fill="none" stroke="currentColor" stroke-width="1.1"/><path d="M1 2.6l5 4 5-4" fill="none" stroke="currentColor" stroke-width="1.1"/></svg>
      <span>renny@rennyosbert.example</span>
    </li>
    <li>
      <svg viewBox="0 0 12 12" aria-hidden="true"><circle cx="6" cy="6" r="5.3" fill="currentColor"/><path d="M0.8 6h10.4M6 0.8c-2 2.8-2 7.6 0 10.4M6 0.8c2 2.8 2 7.6 0 10.4M1.6 3.5h8.8M1.6 8.5h8.8" fill="none" stroke="var(--card-light)" stroke-width=".7"/></svg>
      <span>www.rennyosbert.example</span>
    </li>
  </ul>
</section>

</body>
</html>
```